Postcard: Open Sky Circle

Text for front: HOW TO CHANGE THE WORLD IN ONE [note: the word "one" should be underlined] STEPHint: It's up to you...[Note: add arrow or something to indicate "turn over"]Text for back: You're going to spend your entire life with someone you can never get away from. (Guess who?) Wouldn't you rather that person #OpenSkyCircle than judgmental or critical? BE the change you want to see! Visit www.OpenSkyCircle-hub.example for daily Dawn Pebbles and community. PLEASE JOIN US![Note: add logo to left half of back side]Font preference for text: Josefin sans

Target Market(s)

People who would be attracted to Corvane church - teravian perennist message. It's spiritual without being overtly religious, so the target market is probably early 30s and up but ideally won't turn off Millennials (folks under 30). It should attract attention of people who are open-minded and committed to progressive social change, tired of an atmosphere of hate-mongering and divisiveness.

Requirements
Nice to have
• It would be nice to convey a sense of challenge - there is an idea of "dawn pebbles" so something related to fire/sparks is appropriate. This is meant to evoke a deeper, divine love more than a sense of romantic love. This love is more fierce than fluffy! Yet it calls us to be our best selves.
Should not have
• Please avoid excessive pink - just the logo is enough, as this design needs to appeal to men as well as women.

```html
<!DOCTYPE html>
<html lang="en">
<head>
<meta charset="utf-8">
<title>Open Sky Circle Postcard</title>
<link rel="stylesheet" href="https://fonts.googleapis.com/css2?family=Arimo:wght@400;700&family=Josefin+Sans:wght@600;700&display=swap">
<style>
  :root {
    --backdrop: #2a2a2a;
    --pink: #e0487c;
    --pink-deep: #c93d6e;
    --pink-soft: #f6d3df;
    --white: #ffffff;
    --ink: #111111;
    --bar: #d9d9d9;
  }
  * { margin: 0; padding: 0; box-sizing: border-box; }
  html, body {
    width: 1200px; height: 997px; overflow: hidden;
    background: var(--backdrop);
    font-family: "Arimo", Arial, sans-serif;
  }
  .canvas { position: relative; width: 1200px; height: 997px; }

  .card {
    position: absolute; left: 280px; width: 653px; height: 462px;
    overflow: hidden;
  }
  .card-front {
    top: 32px;
    background: linear-gradient(180deg, #e6e6e6 0%, var(--pink-soft) 28%, #ef8fb0 60%, var(--pink) 100%);
  }
  .card-back {
    top: 521px;
    background: linear-gradient(180deg, #ffffff 0%, #fbe9ef 35%, #eea7bf 70%, var(--pink-deep) 100%);
  }

  /* front */
  .hashtag {
    position: absolute; top: 22px; left: 0; width: 100%;
    text-align: center; color: var(--pink);
    font-weight: 700; font-size: 27px; letter-spacing: 3px;
  }
  .frame { position: absolute; left: 101px; top: 76px; }
  .headline {
    position: absolute; top: 142px; left: 0; width: 100%;
    text-align: center; color: var(--white); font-weight: 700;
  }
  .headline .line { display: block; font-size: 58px; line-height: 62px; letter-spacing: 1px; }
  .headline .line-wide { letter-spacing: 9px; margin-top: 2px; }
  .headline .accent {
    color: var(--ink); text-decoration: underline;
    text-decoration-thickness: 5px; text-underline-offset: 6px;
  }
  .hint {
    position: absolute; top: 414px; left: 178px;
    color: var(--ink); font-weight: 700; font-size: 19px; letter-spacing: 3px;
  }
  .turn-arrows { position: absolute; left: 520px; top: 415px; }

  /* back */
  .brand {
    position: absolute; top: 88px; left: 0; width: 100%;
    display: flex; align-items: center; justify-content: center; gap: 10px;
  }
  .brand-dot { width: 14px; height: 14px; border-radius: 50%; background: var(--pink); }
  .brand-name {
    font-family: "Josefin Sans", sans-serif; font-weight: 700;
    font-size: 24px; color: var(--pink); letter-spacing: 1px;
  }
  .message {
    position: absolute; top: 185px; left: 0; width: 100%;
    text-align: center; color: var(--pink); font-weight: 700;
    font-size: 15px; line-height: 37px;
  }
  .message .call { color: var(--white); }
  .join {
    position: absolute; top: 384px; left: 0; width: 100%;
    text-align: center; color: var(--white); font-weight: 700; font-size: 15px;
  }
  .url-bar {
    position: absolute; left: 19px; top: 410px; width: 618px; height: 38px;
    border-radius: 7px; background: linear-gradient(180deg, #eeeeee, var(--bar));
    display: flex; align-items: center; justify-content: center;
    color: var(--pink-deep); font-weight: 700; font-size: 19px; letter-spacing: 1.5px;
  }
</style>
</head>
<body>
<main class="canvas">
  <section class="card card-front">
    <p class="hashtag">#OpenSkyCircle</p>
    <svg class="frame" width="468" height="320" viewBox="0 0 468 320" aria-hidden="true">
      <path d="M7 55 V7 H461 V55" fill="none" stroke="#111" stroke-width="14"/>
      <path d="M7 257 V313 H461 V257" fill="none" stroke="#111" stroke-width="14"/>
    </svg>
    <h1 class="headline">
      <span class="line">HOW TO CHANGE</span>
      <span class="line">THE WORLD</span>
      <span class="line line-wide">IN <span class="accent">ONE</span> STEP</span>
    </h1>
    <p class="hint">Hint: It's up to you...</p>
    <svg class="turn-arrows" width="96" height="22" viewBox="0 0 96 22" aria-label="Turn over">
      <g fill="none" stroke="#fff" stroke-width="4">
        <path d="M2 3 L10 11 L2 19"/><path d="M14 3 L22 11 L14 19"/>
        <path d="M26 3 L34 11 L26 19"/><path d="M38 3 L46 11 L38 19"/>
        <path d="M50 3 L58 11 L50 19"/><path d="M62 3 L70 11 L62 19"/>
        <path d="M74 3 L82 11 L74 19"/><path d="M86 3 L94 11 L86 19"/>
      </g>
    </svg>
  </section>

  <section class="card card-back">
    <div class="brand">
      <span class="brand-dot"></span>
      <span class="brand-name">Open Sky Circle</span>
    </div>
    <p class="message">
      You're going to spend your entire life with someone you can never<br>
      get away from. (Guess who?) Wouldn't you rather that person<br>
      #OpenSkyCircle than judgmental or critical?<br>
      <span class="call">BE the change you want to see!</span>
    </p>
    <p class="join">Daily Dawn Pebbles and community. PLEASE JOIN US!</p>
    <div class="url-bar">www.OpenSkyCircle-hub.example</div>
  </section>
</main>
</body>
</html>
```